Namibia currently imports 60% of its food. Yield Forward Tarvenia is an initiative which will assist Namibia to become self sustainable in terms of food production. We aim to do this through the development of 3 agricultural production zones which will include farming zones, local farmer assistance, processing and distribution of the final products. Please see our project overview attached.

```html
<!DOCTYPE html>
<html lang="en">
<head>
<meta charset="utf-8">
<title>Yield Forward Tarvenia</title>
<link rel="stylesheet" href="https://fonts.googleapis.com/css2?family=Outfit:wght@400;500&family=Tinos:wght@700&display=swap">
<style>
  :root {
    --navy: #0b3140;
    --green: #0b6b3a;
    --tan: #c4a07e;
    --mist: #eef1f4;
    --ink: #111;
    --white: #fff;
  }
  * { box-sizing: border-box; margin: 0; padding: 0; }
  html, body { width: 1200px; height: 1029px; overflow: hidden; }
  body { position: relative; background: var(--mist); font-family: "Outfit", sans-serif; color: var(--ink); }

  .hero-photo {
    position: absolute; left: 0; top: 0; width: 1200px; height: 610px;
    background:
      radial-gradient(ellipse 260px 160px at 600px 290px, rgba(255,250,170,.95), rgba(255,240,140,0) 100%),
      linear-gradient(180deg, #f4f5f2 0%, #faf6e6 28%, #fbf0c4 40%, #c9d94a 46%, #8fc22a 58%, #5f9a1c 75%, #3f7412 100%);
  }
  .hero-wave { position: absolute; left: 0; top: 500px; width: 1200px; height: 120px; }

  .nav { position: absolute; top: 26px; left: 144px; display: flex; gap: 23px; }
  .nav a { font-size: 12px; font-weight: 500; color: var(--navy); text-decoration: none; }

  .pill {
    position: absolute; display: flex; align-items: center; justify-content: space-between;
    border-radius: 24px; font-size: 12px; font-weight: 500; text-decoration: none;
  }
  .pill .dot {
    width: 22px; height: 22px; border-radius: 50%; display: flex; align-items: center; justify-content: center;
  }
  .pill svg { width: 8px; height: 8px; }
  .contact { left: 930px; top: 16px; width: 128px; height: 39px; padding: 0 6px 0 23px; background: var(--navy); color: var(--white); }
  .contact .dot, .explore .dot { background: var(--tan); }
  .hero-btn { top: 326px; width: 164px; height: 46px; padding: 0 11px 0 21px; background: var(--white); color: var(--navy); }
  .hero-btn .dot { width: 28px; height: 28px; background: var(--green); }
  .needs { left: 424px; }
  .sustain { left: 612px; padding-left: 30px; }

  .brand-name {
    position: absolute; top: 170px; left: 0; width: 1200px; text-align: center;
    font-family: "Tinos", serif; font-weight: 700; font-size: 40px; color: var(--green); letter-spacing: 1px;
  }
  .tagline {
    position: absolute; top: 282px; left: 0; width: 1200px; text-align: center;
    font-family: "Tinos", serif; font-weight: 700; font-size: 22px; color: var(--ink);
  }

  .about-tag { position: absolute; left: 414px; top: 645px; font-family: "Tinos", serif; font-weight: 700; font-size: 13px; color: var(--white); }
  .about-mark {
    position: absolute; left: 141px; top: 700px; width: 386px; height: 230px;
    display: flex; align-items: center; justify-content: center; text-align: center;
    font-family: "Tinos", serif; font-weight: 700; font-size: 54px; line-height: 1.05; color: var(--green);
  }
  .about-title {
    position: absolute; left: 551px; top: 668px;
    font-family: "Tinos", serif; font-weight: 700; font-size: 36px; line-height: 43px; color: var(--green); white-space: nowrap;
  }
  .about-title .accent { color: var(--tan); }
  .about-copy { position: absolute; left: 551px; top: 761px; width: 490px; font-size: 12px; line-height: 23px; }
  .about-copy p + p { margin-top: 4px; }
  .explore { left: 551px; top: 889px; width: 155px; height: 39px; padding: 0 9px 0 20px; background: var(--green); color: var(--white); }

  .footer { position: absolute; left: 141px; top: 985px; width: 919px; border-top: 1px solid #b9bcc0; text-align: center; padding-top: 10px; font-size: 12px; }
</style>
</head>
<body>
  <div class="hero-photo" role="img" aria-label="Sunlit field of young green crops in rows under a bright cloudy sky"></div>
  <svg class="hero-wave" viewBox="0 0 1200 120" preserveAspectRatio="none" aria-hidden="true">
    <path d="M0 93 C120 40 230 15 320 17 C470 20 620 100 780 105 C940 110 1100 80 1200 43 L1200 120 L0 120 Z" fill="#eef1f4"/>
  </svg>

  <nav class="nav">
    <a href="#">Home</a><a href="#">Namibia Needs</a><a href="#">Solutions</a><a href="#">Sustainability</a><a href="#">Education</a>
  </nav>
  <a class="pill contact" href="#">Contact Us <span class="dot"><svg viewBox="0 0 8 8"><path d="M2 1l3 3-3 3" stroke="#fff" fill="none" stroke-width="1"/></svg></span></a>

  <div class="brand-name">Yield Forward Tarvenia</div>
  <h1 class="tagline">AN KVR AGRI-TECH, FOOD SECURITY INITIATIVE</h1>
  <a class="pill hero-btn needs" href="#">Namibia Needs <span class="dot"><svg viewBox="0 0 8 8"><path d="M2 1l3 3-3 3" stroke="#fff" fill="none" stroke-width="1"/></svg></span></a>
  <a class="pill hero-btn sustain" href="#">Sustainability <span class="dot"><svg viewBox="0 0 8 8"><path d="M2 1l3 3-3 3" stroke="#fff" fill="none" stroke-width="1"/></svg></span></a>

  <div class="about-tag">About</div>
  <div class="about-mark">Yield Forward<br>Tarvenia</div>
  <h2 class="about-title">ABOUT<br>YIELD FORWARD <span class="accent">TARVENIA</span></h2>
  <div class="about-copy">
    <p>Namibia currently imports 60% of its food. Yield Forward Tarvenia is an initiative which will assist Namibia to become self sustainable in terms of food production.</p>
    <p>We aim to do this through the development of 3 agricultural production zones which will include farming zones, local farmer assistance, processing and distribution of the final products.</p>
  </div>
  <a class="pill explore" href="#">Explore Our Site <span class="dot"><svg viewBox="0 0 8 8"><path d="M2 1l3 3-3 3" stroke="#fff" fill="none" stroke-width="1"/></svg></span></a>

  <footer class="footer">© 2024 Yield Forward Tarvenia. All Rights Reserved.</footer>
</body>
</html>
```